Poster Design Project - Quill Bar and Restaurant

We require a Horse Racing Carnival poster (Tarrawong Autumn Turf Festival) to showcase the offer at our Bar/Restaurant.

The venue is called QUILL. Our website is www.quillbar-example.com.au

The venue is heavily design focused with significant use of strong graphics and logos.

The poster will need to be printed out in AO size.
Updates

Once again, thank you all for participating in this design creation. We are going to list a number of other poster briefs shortly that will require strong quirky/design graphics. I hope you'll all participate.

I am happy to provide individual responses to queries about specific designs and why they have been unsuccessful.

Overall we were really impressed with the quality of the submissions.

Thanks Gavin

Target Market(s)

Our demographic is 25-35 years old

Industry/Entity Type

Restaurant

Requirements
Must have
• The following copy needs to be incorporated into the poster -

QUILL

AUTUMN TURF FESTIVAL 2011

Lantern Day - 29th October 2011
Champagne breakfast from 9am
Buses to and from the track
$15 bus ticket includes redeemable drink voucher
DJ from 8pm until 3am

Tarrawong Plate Eve - 31st October 2011
Drink specials all night
DJ from 8pm until close

Tarrawong Plate Day - 1st November 2011
Big screen racing live on 3 screens
Cocktail and drinks specials all day
DJ from 4pm

Fillies Gala - 3rd November 2011
DJ from 8pm until close

Closing Run - 5th November 2011
The finishing post - Complimentary glass of sparkling with presentation of race entry ticket
DJ's from 9pm until 3am

For further enquiries and to secure your bus tickets please contact Corinne on 84172059.

178 Wexford Lane, Port Delvin Vic 3902
Tel: 84172059
Twitter: @thequillbar
Facebook: Quill Bar and Restaurant
www.quillbar-example.com.au
Should not have
• No cheesy graphics

```html
<!DOCTYPE html>
<html lang="en">
<head>
<meta charset="utf-8">
<title>Quill – Autumn Turf Festival 2011</title>
<link rel="stylesheet" href="https://fonts.googleapis.com/css2?family=Monoton&family=Poiret+One&family=Oswald:wght@500;700&family=Bungee&family=Cabin:wght@400;500&display=swap">
<style>
  :root {
    --paper-light: #ffffff;
    --paper-edge: #e4e4e4;
    --ink: #1c1c1c;
    --ink-soft: #333333;
    --red: #d62b3a;
    --orange: #f08a1c;
    --yellow: #e9c92a;
    --green: #4aa845;
    --teal: #1f9aa8;
    --purple: #7b3c9a;
    --pink: #d94b8a;
    --rainbow: linear-gradient(90deg, var(--green), var(--teal), var(--purple), var(--pink), var(--red), var(--orange));
  }
  * { margin: 0; padding: 0; box-sizing: border-box; }
  html, body { width: 985px; height: 1200px; overflow: hidden; }
  body {
    position: relative;
    background: radial-gradient(ellipse at 50% 45%, var(--paper-light) 55%, var(--paper-edge) 100%);
    font-family: "Cabin", "Gill Sans", sans-serif;
    color: var(--ink-soft);
  }
  .ornament {
    position: absolute;
    border-radius: 40px;
    opacity: 0.55;
  }
  .ornament--top {
    left: 30px; top: 30px; width: 500px; height: 175px;
    background: linear-gradient(100deg, rgba(214,43,58,.35), rgba(240,138,28,.3), rgba(74,168,69,.3), rgba(123,60,154,.3));
  }
  .ornament--bottom {
    left: 380px; top: 1002px; width: 560px; height: 165px;
    background: linear-gradient(100deg, rgba(31,154,168,.3), rgba(217,75,138,.3), rgba(233,201,42,.3), rgba(214,43,58,.3));
  }
  .festival-title {
    position: absolute;
    left: 560px; top: 70px; width: 340px;
    text-align: center;
    line-height: 1;
  }
  .festival-title__season {
    display: block;
    font-family: "Monoton", "Impact", sans-serif;
    font-size: 62px;
    color: var(--ink);
    letter-spacing: 2px;
  }
  .festival-title__turf {
    display: block;
    font-family: "Poiret One", "Futura", sans-serif;
    font-size: 66px;
    color: var(--ink);
    letter-spacing: 4px;
    margin-top: 2px;
  }
  .festival-title__event {
    display: block;
    font-family: "Oswald", "Impact", sans-serif;
    font-weight: 700;
    font-size: 78px;
    letter-spacing: 3px;
    background: var(--rainbow);
    -webkit-background-clip: text;
    background-clip: text;
    color: transparent;
    margin-top: 2px;
  }
  .festival-title__year {
    display: block;
    font-family: "Bungee", "Impact", sans-serif;
    font-size: 64px;
    color: var(--ink);
    text-align: right;
    margin-top: 4px;
  }
  .race-horses {
    position: absolute;
    left: 365px; top: 325px; width: 290px; height: 85px;
    border-radius: 30px;
    background: linear-gradient(90deg, rgba(214,43,58,.55), rgba(74,168,69,.5), rgba(31,154,168,.5), rgba(123,60,154,.5));
  }
  .schedule-column {
    position: absolute;
    top: 446px;
    width: 380px;
    text-align: center;
  }
  .schedule-column--left { left: 112px; }
  .schedule-column--right { left: 505px; }
  .race-day { margin-bottom: 30px; }
  .schedule-column--right .race-day { margin-bottom: 22px; }
  .race-day__name {
    display: inline-block;
    font-family: "Oswald", "Impact", sans-serif;
    font-weight: 700;
    font-size: 27px;
    text-transform: uppercase;
    letter-spacing: 0.5px;
    background: var(--rainbow);
    -webkit-background-clip: text;
    background-clip: text;
    color: transparent;
    margin-bottom: 6px;
  }
  .race-day__details {
    list-style: none;
    font-size: 20px;
    line-height: 1.28;
    color: var(--ink-soft);
  }
  .enquiries {
    position: absolute;
    left: 68px; top: 862px; width: 255px;
    font-size: 15.5px;
    line-height: 1.3;
  }
  .venue-name {
    position: absolute;
    left: 66px; top: 935px;
    font-family: "Oswald", "Impact", sans-serif;
    font-weight: 700;
    font-size: 50px;
    letter-spacing: 8px;
    color: var(--ink);
    line-height: 1;
  }
  .venue-contact {
    position: absolute;
    left: 68px; top: 1010px;
    font-style: normal;
    font-size: 15.5px;
    line-height: 1.32;
  }
</style>
</head>
<body>
  <div class="ornament ornament--top" role="img" aria-label="Looping multicoloured line ornament"></div>

  <h1 class="festival-title">
    <span class="festival-title__season">AUTUMN</span>
    <span class="festival-title__turf">TURF</span>
    <span class="festival-title__event">FESTIVAL</span>
    <span class="festival-title__year">2011</span>
  </h1>

  <div class="race-horses" role="img" aria-label="Colourful illustration of galloping racehorses and jockeys"></div>

  <section class="schedule-column schedule-column--left">
    <article class="race-day">
      <h2 class="race-day__name">Lantern Day</h2>
      <ul class="race-day__details">
        <li>29th October 2011</li>
        <li>Champagne breakfast from 9am</li>
        <li>Buses to and from the track</li>
        <li>$15 bus ticket includes redeemable</li>
        <li>drink voucher</li>
        <li>DJ from 8pm until 3am</li>
      </ul>
    </article>
    <article class="race-day">
      <h2 class="race-day__name">Tarrawong Plate Day</h2>
      <ul class="race-day__details">
        <li>1st November 2011</li>
        <li>Champagne breakfast from 9am</li>
        <li>Big screen racing live on 3 screens</li>
        <li>Cocktail and drinks specials all day</li>
        <li>DJ from 4pm</li>
      </ul>
    </article>
  </section>

  <section class="schedule-column schedule-column--right">
    <article class="race-day">
      <h2 class="race-day__name">Tarrawong Plate Eve</h2>
      <ul class="race-day__details">
        <li>31st October 2011</li>
        <li>Drink specials all night</li>
        <li>DJ from 8pm until close</li>
      </ul>
    </article>
    <article class="race-day">
      <h2 class="race-day__name">Fillies Gala</h2>
      <ul class="race-day__details">
        <li>3rd November 2011</li>
        <li>Champagne breakfast from 9am</li>
        <li>Buses to and from the track</li>
        <li>$15 bus ticket includes redeemable</li>
        <li>drink voucher</li>
        <li>DJ from 8pm until close</li>
      </ul>
    </article>
    <article class="race-day">
      <h2 class="race-day__name">Closing Run</h2>
      <ul class="race-day__details">
        <li>5th November 2011</li>
        <li>The finishing post - Complimentary</li>
        <li>glass of sparkling with presentation</li>
        <li>of race entry ticket</li>
        <li>DJ's from 9pm until 3am</li>
      </ul>
    </article>
  </section>

  <p class="enquiries">For further enquiries and to secure your bus tickets please contact Corinne on 84172059.</p>

  <div class="venue-name">QUILL</div>

  <address class="venue-contact">
    178 Wexford Lane,<br>
    Port Delvin Vic 3902<br>
    Tel: 84172059<br>
    Twitter: @thequillbar<br>
    Facebook: Quill Bar and Restaurant<br>
    www.quillbar-example.com.au
  </address>

  <div class="ornament ornament--bottom" role="img" aria-label="Looping multicoloured line ornament"></div>
</body>
</html>
```